Security Warning Sign

We have an existing sign that needs an update. I have attached a picture of the current square sign. We need to maintain the same wording. It needs to be professional and appropriate to attach to our customers fence. Also attached is a copy of our building sign which may lend some inspiration and hopefully the ai format will assist. The final sign will be 600mm x 600mmOur website is www.halvorngate.com.au

```html
<!DOCTYPE html>
<html lang="en">
<head>
<meta charset="utf-8">
<title>Warning – Electronic Surveillance Sign</title>
<link href="https://fonts.googleapis.com/css2?family=Anton&family=Open+Sans:wght@400;600;700;800&display=swap" rel="stylesheet">
<style>
  :root {
    --orange: #f07f09;
    --amber: #f6ae05;
    --ink: #1e1e1c;
    --body-text: #3a3a3a;
    --panel: #ffffff;
    --band: #2a2927;
    --band-deep: #1f1e1d;
    --slash-grey: #5a5957;
    --white: #ffffff;
  }
  html, body {
    margin: 0;
    padding: 0;
    overflow: hidden;
    background: #ffffff;
  }
  .sign {
    position: relative;
    width: 1200px;
    height: 1200px;
    overflow: hidden;
    font-family: "Open Sans", sans-serif;
  }
  .sign__backdrop {
    position: absolute;
    inset: 0;
    background: linear-gradient(160deg, var(--amber) 0%, #f39a06 45%, var(--orange) 80%);
  }
  .sign__headline {
    position: absolute;
    left: 0;
    top: 0;
    width: 1200px;
    height: 260px;
  }
  .sign__headline text {
    font-family: "Anton", "Impact", sans-serif;
    fill: var(--ink);
  }
  .message-panel {
    position: absolute;
    left: 42px;
    top: 268px;
    width: 1108px;
    height: 602px;
    background: var(--panel);
  }
  .message-panel__text {
    margin: 0;
    padding-top: 38px;
    text-align: center;
    font-weight: 400;
    font-size: 90px;
    line-height: 138px;
    color: var(--body-text);
    letter-spacing: -1px;
  }
  .message-panel__text span { display: block; }
  .brand-band {
    position: absolute;
    left: 42px;
    top: 870px;
    width: 1108px;
    height: 288px;
    background: linear-gradient(135deg, var(--band) 0%, var(--band-deep) 100%);
  }
  .brand {
    position: absolute;
    left: 344px;
    top: 52px;
    display: flex;
    align-items: center;
    gap: 26px;
  }
  .brand__mark {
    width: 124px;
    height: 124px;
    border-radius: 50%;
    background: var(--orange);
    flex: none;
  }
  .brand__name {
    font-weight: 800;
    font-size: 44px;
    line-height: 48px;
    color: var(--white);
    letter-spacing: 1px;
  }
  .brand__name span { display: block; }
  .contact-strip {
    position: absolute;
    left: 0;
    bottom: 0;
    width: 1108px;
    height: 74px;
  }
  .contact-strip__web {
    position: absolute;
    left: 110px;
    top: 20px;
    font-weight: 700;
    font-size: 29px;
    color: var(--white);
    letter-spacing: 0.3px;
  }
  .contact-strip__shapes {
    position: absolute;
    inset: 0;
  }
  .contact-strip__phone {
    position: absolute;
    left: 700px;
    top: 4px;
    display: flex;
    align-items: center;
    gap: 10px;
    font-weight: 800;
    font-size: 54px;
    line-height: 64px;
    color: var(--white);
    letter-spacing: -0.5px;
  }
  .contact-strip__phone svg { width: 40px; height: 40px; }
</style>
</head>
<body>
  <div class="sign">
    <div class="sign__backdrop" role="img" aria-label="Orange and amber faceted geometric background"></div>

    <svg class="sign__headline" viewBox="0 0 1200 260" aria-label="Warning">
      <text x="64" y="232" font-size="228" textLength="1056" lengthAdjust="spacingAndGlyphs">WARNING</text>
    </svg>

    <section class="message-panel">
      <p class="message-panel__text">
        <span>ELECTRONIC</span>
        <span>SURVEILLANCE AND</span>
        <span>RECORDING DEVICES</span>
        <span>INSTALLED IN THIS AREA</span>
      </p>
    </section>

    <section class="brand-band">
      <div class="brand">
        <div class="brand__mark"></div>
        <div class="brand__name">
          <span>HALVORN</span>
          <span>GATE</span>
          <span>SECURITY</span>
        </div>
      </div>

      <div class="contact-strip">
        <svg class="contact-strip__shapes" viewBox="0 0 1108 74" preserveAspectRatio="none" aria-hidden="true">
          <polygon points="640,74 648,74 690,14 682,14" fill="var(--slash-grey)"/>
          <polygon points="652,74 664,74 706,14 694,14" fill="var(--orange)"/>
          <polygon points="670,74 1108,74 1108,0 722,0" fill="var(--orange)"/>
        </svg>
        <div class="contact-strip__web">WWW.HALVORNGATE.COM.AU</div>
        <div class="contact-strip__phone">
          <svg viewBox="0 0 24 24" aria-hidden="true">
            <path fill="#ffffff" d="M6.6 10.8a15.1 15.1 0 0 0 6.6 6.6l2.2-2.2a1 1 0 0 1 1-.25 11.4 11.4 0 0 0 3.6.57 1 1 0 0 1 1 1V20a1 1 0 0 1-1 1A17 17 0 0 1 3 4a1 1 0 0 1 1-1h3.5a1 1 0 0 1 1 1c0 1.25.2 2.45.57 3.57a1 1 0 0 1-.25 1z"/>
          </svg>
          <span>1300 471 286</span>
        </div>
      </div>
    </section>
  </div>
</body>
</html>
```